General brochure with course listing

A general brochure for the Global Jurist Academy, about 40 A5 pages that includes mission, vision, history, descriptions of our technical assistance and capacity building programming and detailed descriptions of our courses. Would be for both online pdf (magazine style) and print. I have attached an example of an older one that was satisfactory but not as professional as what we're looking for now.

Target Market(s)

Lawyers and government officials around the world.

Industry/Entity Type

Legal and capacity building

Requirements
Must have
• A good design and template that we can replicate on our own in InDesign annually. We need the layout from you and we will provide the copy. We will also publish as a pdf
Nice to have
• Colors and branding from our website - www.gja-example.org

```html
<!DOCTYPE html>
<html lang="en">
<head>
<meta charset="utf-8">
<title>Global Jurist Academy — 2024 Announcement of Programs</title>
<link rel="stylesheet" href="https://fonts.googleapis.com/css2?family=Crimson+Pro:ital,wght@0,400;0,600;0,700;1,400&family=Montserrat:wght@400;500;600;700;800&display=swap">
<style>
  :root {
    --navy: #2d3a6b;
    --coral: #f07e5c;
    --sky: #80b1d9;
    --photo: #6ea3d1;
    --mist: #eef1f5;
    --paper: #ffffff;
    --backdrop: #e8e5e0;
    --ink: #222a44;
  }
  * { box-sizing: border-box; margin: 0; padding: 0; }
  html, body { width: 1200px; height: 821px; overflow: hidden; }
  body { background: var(--backdrop); font-family: "Montserrat", sans-serif; position: relative; }

  .page { position: absolute; width: 526px; height: 370px; overflow: hidden; box-shadow: 2px 3px 8px rgba(0,0,0,.25); }
  .page svg.shapes { position: absolute; inset: 0; }

  /* Cover */
  .cover { left: 49px; top: 26px; background: var(--paper); }
  .cover .brand { position: absolute; left: 37px; top: 52px; display: flex; align-items: center; gap: 6px; }
  .cover .brand-dot { width: 12px; height: 12px; border-radius: 50%; background: var(--navy); }
  .cover .brand-name { font-family: "Crimson Pro", serif; font-weight: 600; font-size: 13px; color: var(--navy); width: 80px; line-height: 1.1; }
  .cover .year { position: absolute; left: 31px; top: 148px; font-family: "Crimson Pro", serif; font-weight: 700; font-size: 66px; line-height: 1; color: var(--coral); letter-spacing: 1px; }
  .cover .title { position: absolute; left: 33px; top: 216px; font-family: "Crimson Pro", serif; font-weight: 700; font-size: 16.5px; color: var(--navy); }
  .cover .subtitle { position: absolute; left: 33px; top: 238px; font-family: "Crimson Pro", serif; font-size: 12px; line-height: 15px; color: var(--navy); }
  .cover .bar-name { position: absolute; left: 24px; top: 316px; color: #fff; font-weight: 800; font-size: 12.5px; }
  .cover .bar-tagline { position: absolute; left: 24px; top: 333px; color: var(--sky); font-weight: 600; font-size: 6.3px; }

  /* Contents */
  .contents { left: 619px; top: 26px; background: var(--navy); }
  .contents h2 { position: absolute; left: 37px; top: 24px; font-family: "Crimson Pro", serif; font-weight: 700; font-size: 29px; color: var(--coral); }
  .toc { position: absolute; left: 42px; top: 68px; width: 228px; list-style: none; }
  .toc li { display: flex; align-items: baseline; height: 13.3px; font-size: 7.9px; color: #fff; }
  .toc li.gap { margin-top: 13.3px; }
  .toc .leader { flex: 1; border-bottom: 0.6px dotted rgba(255,255,255,.8); margin: 0 1px; transform: translateY(-2px); }
  .toc .num { font-size: 7.4px; }
  .toc .num.badge { background: var(--coral); border-radius: 50%; width: 10px; height: 10px; display: inline-flex; align-items: center; justify-content: center; font-size: 6.3px; align-self: center; }

  /* Course page */
  .course-page { left: 326px; top: 419px; background: var(--paper); }
  .course-page .section-label { position: absolute; left: 0; top: 0; width: 140px; height: 59px; display: flex; align-items: center; justify-content: center; font-family: "Crimson Pro", serif; font-weight: 700; font-size: 15px; color: #fff; }
  .course-head { position: absolute; left: 152px; top: 11px; width: 360px; }
  .course-head h3 { font-size: 9px; font-weight: 700; color: var(--navy); display: flex; align-items: center; gap: 4px; }
  .course-head .date { background: var(--sky); color: #fff; font-size: 6px; font-weight: 700; padding: 1px 4px; }
  .course-head p { font-size: 5.6px; line-height: 7.5px; color: var(--ink); margin-top: 2px; }
  .topic { position: absolute; }
  .topic h4 { font-size: 5.9px; font-weight: 700; color: var(--navy); display: flex; align-items: center; gap: 3px; margin-bottom: 8px; }
  .topic h4::before { content: ""; width: 5px; height: 5px; border-radius: 50%; background: var(--coral); margin-left: -1px; }
  .topic p { font-size: 6.2px; line-height: 7.45px; color: var(--ink); text-align: justify; }
  .col-left { left: 40px; width: 192px; }
  .col-right { left: 272px; width: 215px; }
  .row-1 { top: 80px; } .row-2 { top: 156px; } .row-3 { top: 233px; }
  .closing { position: absolute; left: 40px; top: 307px; width: 440px; font-size: 5.9px; line-height: 7.3px; color: var(--ink); }
  .folio { position: absolute; left: 497px; top: 339px; font-family: "Crimson Pro", serif; font-style: italic; font-size: 14px; color: var(--navy); }
</style>
</head>
<body>

<section class="page cover">
  <svg class="shapes" width="526" height="370" viewBox="0 0 526 370">
    <defs>
      <linearGradient id="photoTone" x1="0" y1="0" x2="1" y2="1">
        <stop offset="0" stop-color="#7db0dc"/>
        <stop offset=".55" stop-color="#6a9fcf"/>
        <stop offset="1" stop-color="#a9cbe8"/>
      </linearGradient>
    </defs>
    <polygon points="185,0 320,0 253,205" fill="var(--sky)"/>
    <polygon points="329,0 526,0 526,370 204,370" fill="url(#photoTone)" role="img" aria-label="Photo of smiling workshop participants seated at a conference table, tinted blue"/>
    <polygon points="0,300 221,300 197,370 0,370" fill="var(--navy)"/>
  </svg>
  <div class="brand"><span class="brand-dot"></span><span class="brand-name">Global Jurist Academy</span></div>
  <div class="year">2024</div>
  <div class="title">Announcement of Programs</div>
  <div class="subtitle">Training in Finance, Management,<br>Law and Governance</div>
  <div class="bar-name">Global Jurist Academy</div>
  <div class="bar-tagline">Advancing Justice Through Shared Knowledge</div>
</section>

<section class="page contents">
  <svg class="shapes" width="526" height="370" viewBox="0 0 526 370">
    <polygon points="526,0 526,370 370,370" fill="var(--sky)"/>
  </svg>
  <h2>Contents</h2>
  <ul class="toc">
    <li>Executive Director’s Welcome<span class="leader"></span><span class="num">2</span></li>
    <li>GJA: Advancing Justice Through Shared Knowledge<span class="leader"></span><span class="num">3</span></li>
    <li>Technical Assistance<span class="leader"></span><span class="num">4</span></li>
    <li>Why the GJA?<span class="leader"></span><span class="num">5</span></li>
    <li>Faculty and Staff<span class="leader"></span><span class="num">6</span></li>
    <li>Evaluations<span class="leader"></span><span class="num">8</span></li>
    <li>Publishing<span class="leader"></span><span class="num">9</span></li>
    <li>Centers of Expertise<span class="leader"></span><span class="num">10</span></li>
    <li>Regional Centers<span class="leader"></span><span class="num">16</span></li>
    <li class="gap">Procurement and Project Life Cycle Courses<span class="leader"></span><span class="num badge">18</span></li>
    <li>Alternative Dispute Resolution Courses<span class="leader"></span><span class="num badge">26</span></li>
    <li>Finance Courses<span class="leader"></span><span class="num badge">31</span></li>
    <li>Legislative Courses<span class="leader"></span><span class="num badge">33</span></li>
    <li>Governance and Judicial Administration Courses<span class="leader"></span><span class="num badge">36</span></li>
    <li>Additional Offerings<span class="leader"></span><span class="num badge">39</span></li>
    <li>Customized Training<span class="leader"></span><span class="num badge">45</span></li>
    <li>Registration Information<span class="leader"></span><span class="num badge">46</span></li>
  </ul>
</section>

<section class="page course-page">
  <svg class="shapes" width="526" height="370" viewBox="0 0 526 370">
    <rect x="0" y="0" width="526" height="59" fill="var(--mist)"/>
    <polygon points="0,0 147,0 127,59 0,59" fill="var(--navy)"/>
    <rect x="505" y="34" width="21" height="287" fill="var(--sky)"/>
    <line x1="0" y1="349.5" x2="486" y2="349.5" stroke="var(--navy)" stroke-width="1"/>
  </svg>
  <div class="section-label">Finance Courses</div>
  <header class="course-head">
    <h3>International Borrowing and Debt Management <span class="date">April 2-13</span></h3>
    <p>This seminar explores key topics with respect to international borrowing and debt management.<br>The goal is to assist policy makers and practitioners from emerging economies to plan for long term challenges,<br>in a fast changing international borrowing and debt management environment.</p>
  </header>

  <article class="topic col-left row-1"><h4>LOREM IPSUM DOLOR SIT AMET, CONSECTETUR.</h4><p>Lorem ipsum dolor sit amet, consectetur adipiscing elit. Quisque sodales ligula nec odio viverra ullamcorper. Maecenas id lorem lacinia nisi blandit laoreet eu ac nunc. Mauris semper tincidunt urna eget cursus. Nullam ac mi porta, dictum ipsum vestibulum, condimentum metus. In maximus risus nec tincidunt rutrum.</p></article>
  <article class="topic col-right row-1"><h4>LOREM IPSUM DOLOR SIT AMET, CONSECTETUR.</h4><p>Lorem ipsum dolor sit amet, consectetur adipiscing elit. Quisque sodales ligula nec odio viverra ullamcorper. Maecenas id lorem lacinia nisi blandit laoreet eu ac nunc. Mauris semper tincidunt urna eget cursus. Nullam ac mi porta, dictum ipsum vestibulum, condimentum metus. In maximus risus nec tincidunt rutrum.</p></article>
  <article class="topic col-left row-2"><h4>LOREM IPSUM DOLOR SIT AMET, CONSECTETUR.</h4><p>Lorem ipsum dolor sit amet, consectetur adipiscing elit. Quisque sodales ligula nec odio viverra ullamcorper. Maecenas id lorem lacinia nisi blandit laoreet eu ac nunc. Mauris semper tincidunt urna eget cursus. Nullam ac mi porta, dictum ipsum vestibulum, condimentum metus. In maximus risus nec tincidunt rutrum.</p></article>
  <article class="topic col-right row-2"><h4>LOREM IPSUM DOLOR SIT AMET, CONSECTETUR.</h4><p>Lorem ipsum dolor sit amet, consectetur adipiscing elit. Quisque sodales ligula nec odio viverra ullamcorper. Maecenas id lorem lacinia nisi blandit laoreet eu ac nunc. Mauris semper tincidunt urna eget cursus. Nullam ac mi porta, dictum ipsum vestibulum, condimentum metus. In maximus risus nec tincidunt rutrum.</p></article>
  <article class="topic col-left row-3"><h4>LOREM IPSUM DOLOR SIT AMET, CONSECTETUR.</h4><p>Lorem ipsum dolor sit amet, consectetur adipiscing elit. Quisque sodales ligula nec odio viverra ullamcorper. Maecenas id lorem lacinia nisi blandit laoreet eu ac nunc. Mauris semper tincidunt urna eget cursus. Nullam ac mi porta, dictum ipsum vestibulum, condimentum metus. In maximus risus nec tincidunt rutrum.</p></article>
  <article class="topic col-right row-3"><h4>LOREM IPSUM DOLOR SIT AMET, CONSECTETUR.</h4><p>Lorem ipsum dolor sit amet, consectetur adipiscing elit. Quisque sodales ligula nec odio viverra ullamcorper. Maecenas id lorem lacinia nisi blandit laoreet eu ac nunc. Mauris semper tincidunt urna eget cursus. Nullam ac mi porta, dictum ipsum vestibulum, condimentum metus. In maximus risus nec tincidunt rutrum.</p></article>

  <p class="closing">Ut lacus libero, hendrerit ac sapien sed, placerat gravida elit. Duis cursus arcu vitae pretium convallis. Integer auctor tellus est, eu fermentum mi semper in. Morbi eget risus ultricies, dignissim neque sed, elementum turpis. Etiam et dui at velit volutpat egestas id non diam. Maecenas ac lectus interdum lorem molestie ultrices. Vestibulum suscipit arcu magna,</p>
  <div class="folio">31</div>
</section>

</body>
</html>
```